Newsletter für Hersteller von beleuchteten und unbeleuchteten Spiegeln
Zielgruppe
Wir sind Hersteller von beleuchteten und unbeleuchteten Spiegeln. Wir machen bei uns in Bünde vom Zuschnitt, über Design bis hin zum Aufbau der Technik alles selber.
Aufgabenstellung
Erstellung einer E-Mail-Vorlage für Angebote. Es muss erkennbar bleiben, dass es ein Angebot ist, es soll nicht aussehen wie ein Newsletter. Der bisherige Text kann überarbeitet werden.
Erforderliche Bilder bitte von der Website nehmen. Die Vorlage muss responsiv sein.
Außerdem sollen im unteren Bereich 4-6 Bilder sein & unser Standort mitten in DEUTSCHLAND mit Link zu Ortfinder-Web, folgende Links sollen ebenso enthalten sein:
https://www.vandorf-lumoglas.com/ratgeber/spiegel-korrosion-vermeiden
https://www.vandorf-lumoglas.com/ratgeber/vergleich-badspiegel-beleuchtung-und-lichtstaerke
https://www.vandorf-lumoglas.com/unternehmen
https://www.vandorf-lumoglas.com/kundenbilder
https://www.vandorf-lumoglas.com/ratgeber/warum-sie-ihren-badspiegel-bei-vandorf-lumoglas-kaufen-sollten
https://www.ortfinder-web.net/ort/Vandorf+Lumoglas-Atelier-GmbH
https://www.bildnetz-social.net/p/QwRtZ8kLmNp/
ggf. soll das Gesicht unseres Telefonisten hier gezeigt werden: https://www.vandorf-lumoglas.com/spiegel/
ggf aber auch nur ein Icon vom Telefon
Oben soll ein Logo sein

```html
<!DOCTYPE html>
<html lang="de">
<head>
<meta charset="utf-8">
<title>Ihr persönliches Angebot – Vandorf Lumoglas-Atelier</title>
<link href="https://fonts.googleapis.com/css2?family=Manrope:wght@400;500;600&display=swap" rel="stylesheet">
<style>
  :root {
    --ink: #111111;
    --paper: #ffffff;
    --photo-office: #cfd8de;
    --photo-office-dark: #8fa7b5;
    --tile-1a: #2b2e33; --tile-1b: #6b6f73;
    --tile-2a: #8a8a88; --tile-2b: #5d4a3a;
    --tile-3a: #d9d6d2; --tile-3b: #8a6a4c;
    --tile-4a: #e3e8ea; --tile-4b: #c8d0d3;
  }
  * { margin: 0; padding: 0; box-sizing: border-box; }
  html, body { width: 719px; height: 1200px; overflow: hidden; background: var(--paper); }
  body { font-family: "Manrope", sans-serif; color: var(--ink); position: relative; }
  .offer-mail { position: relative; width: 719px; height: 1200px; }
  .abs { position: absolute; }
  .title { left: 0; width: 719px; top: 50px; text-align: center; font-size: 38px; font-weight: 500; letter-spacing: 0.2px; }
  .meta { left: 118px; top: 131px; font-size: 18px; line-height: 23px; }
  .salutation { left: 118px; top: 253px; font-size: 18px; }
  .intro { left: 118px; top: 315px; font-size: 18px; line-height: 23px; }
  .section-head { font-size: 17px; font-weight: 600; }
  .questions-head { left: 118px; top: 432px; }
  .agent-photo { left: 117px; top: 473px; width: 125px; height: 124px;
    background: linear-gradient(135deg, var(--photo-office) 0%, #eef2f4 45%, var(--photo-office-dark) 100%); }
  .contact { left: 265px; font-size: 18px; }
  .contact-team { top: 473px; }
  .contact-line { display: flex; align-items: center; gap: 12px; }
  .contact-phone { top: 525px; }
  .contact-mail { top: 571px; }
  .contact-line svg { width: 18px; height: 18px; flex: none; }
  .inspiration-head { left: 119px; top: 671px; }
  .inspiration-lead { left: 119px; top: 706px; font-size: 18px; }
  .resource-links { left: 119px; top: 741px; list-style: none; font-size: 16px; line-height: 21.5px; }
  .resource-links a { color: var(--ink); text-decoration: none; }
  .social-link { display: flex; align-items: center; gap: 5px; }
  .social-mark { width: 13px; height: 13px; border: 1.6px solid var(--ink); border-radius: 3px; }
  .gallery { left: 117px; top: 916px; display: flex; gap: 15px; }
  .gallery-tile { width: 108px; height: 83px; }
  .tile-1 { background: linear-gradient(135deg, var(--tile-1a), var(--tile-1b)); }
  .tile-2 { background: linear-gradient(180deg, var(--tile-2a), var(--tile-2b)); }
  .tile-3 { background: linear-gradient(180deg, var(--tile-3a), var(--tile-3b)); }
  .tile-4 { background: linear-gradient(135deg, var(--tile-4a), var(--tile-4b)); }
  .location { left: 158px; top: 1071px; display: flex; align-items: center; gap: 8px; font-size: 19px; }
  .location svg { width: 16px; height: 20px; margin-top: 10px; }
  .location a { color: var(--ink); text-decoration: none; }
  .company-footer { left: 119px; top: 1138px; font-size: 16px; }
</style>
</head>
<body>
<main class="offer-mail">
  <h1 class="abs title">Ihr persönliches Angebot</h1>

  <p class="abs meta">Angebotsnummer: AN462490<br>Kundennummer: 299176</p>

  <p class="abs salutation">Sehr geehrte Damen und Herren,</p>
  <p class="abs intro">vielen Dank für Ihre Anfrage. Ihr individuelles Angebot<br>finden Sie im Anhang dieser E-Mail.</p>

  <h2 class="abs section-head questions-head">Haben Sie Fragen?</h2>
  <div class="abs agent-photo" role="img" aria-label="Foto: Mitarbeiter am Telefon im hellen Büro"></div>
  <p class="abs contact contact-team">Unser Team ist gerne für Sie da.</p>
  <p class="abs contact contact-line contact-phone">
    <svg viewBox="0 0 24 24" aria-hidden="true"><path fill="currentColor" d="M6.6 10.8a15.1 15.1 0 0 0 6.6 6.6l2.2-2.2a1 1 0 0 1 1-.25 11.4 11.4 0 0 0 3.6.57 1 1 0 0 1 1 1V20a1 1 0 0 1-1 1A17 17 0 0 1 3 4a1 1 0 0 1 1-1h3.5a1 1 0 0 1 1 1c0 1.25.2 2.45.57 3.57a1 1 0 0 1-.25 1z"/></svg>
    Telefon: +49 5223 4417302
  </p>
  <p class="abs contact contact-line contact-mail">
    <svg viewBox="0 0 24 24" aria-hidden="true"><path fill="currentColor" d="M2 5h20v14H2z"/><path d="M2 5l10 8 10-8M2 19l7.5-7M22 19l-7.5-7" stroke="#fff" stroke-width="1.6" fill="none"/></svg>
    E-Mail: info@vandorf-lumoglas.com
  </p>

  <h2 class="abs section-head inspiration-head">Inspiration &amp; Informationen</h2>
  <p class="abs inspiration-lead">Hier finden Sie nützliche Tipps und Einblicke:</p>
  <ul class="abs resource-links">
    <li><a href="https://www.vandorf-lumoglas.com/ratgeber/spiegel-korrosion-vermeiden">Spiegel-Korrosion vermeiden</a></li>
    <li><a href="https://www.vandorf-lumoglas.com/ratgeber/vergleich-badspiegel-beleuchtung-und-lichtstaerke">Vergleich Badspiegel: Beleuchtung und Lichtstärke</a></li>
    <li><a href="https://www.vandorf-lumoglas.com/unternehmen">Über uns</a></li>
    <li><a href="https://www.vandorf-lumoglas.com/kundenbilder">Kundenbilder</a></li>
    <li><a class="social-link" href="https://www.bildnetz-social.net/p/QwRtZ8kLmNp/"><span class="social-mark"></span>Besuchen Sie uns auch auf Bildnetz</a></li>
  </ul>

  <div class="abs gallery">
    <div class="gallery-tile tile-1" role="img" aria-label="Foto: dunkles Bad mit beleuchtetem Spiegel"></div>
    <div class="gallery-tile tile-2" role="img" aria-label="Foto: Bad mit großem LED-Spiegel über Holzwaschtisch"></div>
    <div class="gallery-tile tile-3" role="img" aria-label="Foto: heller Waschtisch mit breitem Spiegel"></div>
    <div class="gallery-tile tile-4" role="img" aria-label="Foto: Kosmetikspiegel auf Ablage"></div>
  </div>

  <p class="abs location">
    <svg viewBox="0 0 16 20" aria-hidden="true"><path fill="currentColor" d="M8 0a7 7 0 0 0-7 7c0 5 7 13 7 13s7-8 7-13a7 7 0 0 0-7-7zm0 9.5A2.5 2.5 0 1 1 8 4.5a2.5 2.5 0 0 1 0 5z"/></svg>
    <a href="https://www.ortfinder-web.net/ort/Vandorf+Lumoglas-Atelier-GmbH">Hier finden Sie uns in Bünde, Deutschland</a>
  </p>

  <p class="abs company-footer">Vandorf Lumoglas-Atelier GmbH |Lichtgasse 4-9 | 32257 Bünde</p>
</main>
</body>
</html>
```